Project Managers Business card design

We need business cards for our Project Managers based in Sydney for our business name Korbet Pty Ltd. We project manage property improvements and infrastructure Assets. We provide asset owners Project Management services from original concept, management of architectural and engineering designs, call and select construction tenders, and manage the Asset operational life cycle to conclusion and removal. We are experienced in feasibility studies, risk assessments, quality control, safety control, environmental analysis. We are specialist in Aged Care and Child Care Services. We can provide asset reviewing checklists, asset inspections, contract cost and contract assessments, dispute resolution services and articles and books on safely working and living in environments subject to analysis. the design colours should be queensland marone and NSW sky blue.

Industry/Entity Type

Construction

Contact Information for Business Card

Gavin Trelowe (Mb 0412 847 391), Dennis Marquay (Mb 0438 216 074), Luke Benhadda,(Mb 0421 963 158)
E: all business cards: korbet@fernmail.example
Office phone number (02) 9482 3165
Address
Level 1 Halyard House
47 Wexford Lane, Parramatta
Web: projectmanagers@worksleadsbykorbet.example (to be checked on Printlyne web draft)

```html
<!DOCTYPE html>
<html lang="en">
<head>
<meta charset="utf-8">
<title>Korbet Pty Ltd – Business Card</title>
<link rel="stylesheet" href="https://fonts.googleapis.com/css2?family=Exo+2:ital,wght@1,800&family=Arimo:wght@400&display=swap">
<style>
  :root {
    --backdrop: #6a6d67;
    --card-top-light: #b4b5b0;
    --card-top-dark: #8e908b;
    --card-foot: #b0b49c;
    --card-foot-light: #c3c6b2;
    --band: #000000;
    --name-ink: #0b0b0b;
    --contact-ink: #ffffff;
    --address-ink: #1a1a1a;
  }
  html, body {
    margin: 0;
    padding: 0;
    width: 1200px;
    height: 902px;
    overflow: hidden;
    background: var(--backdrop);
  }
  .card {
    position: absolute;
    left: 100px;
    top: 166px;
    width: 1000px;
    height: 570px;
    border-radius: 30px;
    overflow: hidden;
    box-shadow: 0 18px 40px rgba(0,0,0,0.28);
  }
  .card-shapes {
    position: absolute;
    inset: 0;
    display: block;
  }
  .holder-name {
    position: absolute;
    left: 0;
    right: 0;
    top: 70px;
    margin: 0;
    text-align: center;
    font-family: "Exo 2", sans-serif;
    font-style: italic;
    font-weight: 800;
    font-size: 76px;
    letter-spacing: 2px;
    color: var(--name-ink);
  }
  .contact-list {
    position: absolute;
    left: 0;
    right: 0;
    top: 262px;
    margin: 0;
    padding: 0;
    list-style: none;
    text-align: center;
    font-family: "Arimo", sans-serif;
    font-size: 30px;
    line-height: 44px;
    color: var(--contact-ink);
  }
  .office-address {
    position: absolute;
    left: 0;
    right: 0;
    top: 508px;
    margin: 0;
    text-align: center;
    font-family: "Arimo", sans-serif;
    font-style: normal;
    font-size: 28px;
    color: var(--address-ink);
  }
</style>
</head>
<body>
  <div class="card">
    <svg class="card-shapes" width="1000" height="570" viewBox="0 0 1000 570" aria-hidden="true">
      <defs>
        <linearGradient id="top-panel" x1="0" y1="0" x2="1" y2="0.4">
          <stop offset="0" stop-color="var(--card-top-dark)"/>
          <stop offset="1" stop-color="var(--card-top-light)"/>
        </linearGradient>
        <linearGradient id="foot-panel" x1="0" y1="0" x2="0" y2="1">
          <stop offset="0" stop-color="var(--card-foot-light)"/>
          <stop offset="1" stop-color="var(--card-foot)"/>
        </linearGradient>
      </defs>
      <rect class="card-base" x="0" y="0" width="1000" height="570" fill="url(#top-panel)"/>
      <rect class="card-foot" x="0" y="400" width="1000" height="170" fill="url(#foot-panel)"/>
      <path class="contact-band" d="M0 170 Q500 308 1000 170 L1000 522 Q500 396 0 522 Z" fill="var(--band)"/>
    </svg>

    <h1 class="holder-name">Gavin Trelowe</h1>

    <ul class="contact-list">
      <li>M 0412 847 391</li>
      <li>P (02) 9482 3165</li>
      <li>E korbet@fernmail.example</li>
      <li>W www.worksleadsbykorbet.example</li>
    </ul>

    <address class="office-address">Level 1 Halyard House 47 Wexford Lane, Parramatta</address>
  </div>
</body>
</html>
```